BRVL Brochure Design

Northfield Council of Clinical Standards (BRVL) needs a whole new brochure. I've upload EPS logos and past brochures. Our tagline is to "modernize healthcare" and we think our brochure should reflect that, so that's the purpose of this project.

BRVL is a proven leader in healthcare education, training and
consulting services for health professionals. We’ve earned a reputation for excellence in healthcare quality improvement and management.

BRVL works to improve healthcare quality by educating healthcare professionals about healthcare best practices. We focus on instructing our clients on how to plan for, measure, and improve healthcare quality in all facilities and facets such as:

Patient Safety
Infection Control
Performance Improvement
Risk Management
Compliance and Accreditation
Health and Hospital Administration
Health Insurance
Healthcare Financial Management
Facility Management and Safety

DESIGN SUGGESTIONS:

Brochure Size: 8.5 X 11 full size brochure or 8.5 X 11 trifold brochure

Number of Pages: 2 to 3

Colors: Feel free to use a wide array of colors but try to stay away from colors that are too loud, ex: Pink, Purple, Neon Green.

Themes: Professional, Educational

Designs:

Pelor by Oskar Lindqvist

Quorvo Pamphlet by Derek Malloway

Lanterns for harvest by Solvendri

Paisaje de Sr KT by vrpl

http://www.plimbask.com/post/28461937205/10-creative-brochure-designs

Don't limit yourself to these examples. However, these are examples we liked

Reason: We would like to see more designs

We want more full page designs than tri-fold 

We are considering both tri-fold and full-page but would like to see more full page designs 

Reason: Our lead designer making the decisions on this project has been fired. I apologize for the inconvenience. We want extend the project one last time

Target Market(s)

Students, Doctors, and Educational Professionals

Industry/Entity Type

Healthcare

Logo Text

asdfasdf

Font styles to use
Serif
Sans Serif
Decorative
Script

Requirements
Should not have
• Pink, Purple, Neon Green colors

```html
<!DOCTYPE html>
<html lang="en">
<head>
<meta charset="utf-8">
<title>BRVL Brochure – Outside Spread</title>
<link rel="stylesheet" href="https://fonts.googleapis.com/css2?family=Montserrat:wght@700;800&family=Nunito+Sans:wght@300;400;700;800&display=swap">
<style>
  :root {
    --navy: #1b3c8c;
    --navy-deep: #14306f;
    --cyan: #2fb3e3;
    --sky: #8fd3f0;
    --ink: #3a3f4a;
    --paper: #ffffff;
  }
  * { margin: 0; padding: 0; box-sizing: border-box; }
  html, body { width: 1200px; height: 853px; overflow: hidden; background: var(--paper); }
  .spread {
    position: relative;
    width: 1200px;
    height: 853px;
    background: var(--paper);
    font-family: "Nunito Sans", Arial, sans-serif;
    color: var(--ink);
    overflow: hidden;
  }
  .art { position: absolute; inset: 0; width: 1200px; height: 853px; }

  .section-title {
    font-family: "Montserrat", Arial, sans-serif;
    font-weight: 800;
    font-size: 33px;
    color: var(--navy);
    letter-spacing: 0.3px;
    margin-bottom: 26px;
  }
  .section-body {
    font-size: 12.6px;
    line-height: 19px;
    color: var(--ink);
  }
  .section-body strong { color: var(--navy); font-weight: 800; }

  .vision { position: absolute; left: 60px; top: 80px; width: 310px; }
  .mission { position: absolute; left: 450px; top: 80px; width: 300px; }

  .quote {
    position: absolute;
    left: 420px; top: 395px;
    width: 380px;
    text-align: center;
    color: var(--navy);
  }
  .quote-mark {
    position: absolute;
    font-family: "Montserrat", Arial, sans-serif;
    font-weight: 800;
    font-size: 90px;
    color: var(--sky);
    line-height: 1;
  }
  .quote-mark.open { left: 0; top: -8px; }
  .quote-mark.close { right: 0; top: 40px; }
  .quote-line { font-size: 31px; font-weight: 300; line-height: 36px; }
  .quote-line.strong { font-weight: 800; }
  .quote-author {
    font-size: 10px; letter-spacing: 1px; font-weight: 700;
    color: var(--cyan); margin-top: 4px; padding-left: 120px;
  }

  .contact {
    position: absolute;
    left: 470px; top: 638px;
    width: 300px;
    text-align: center;
    color: var(--navy-deep);
  }
  .contact-title {
    font-family: "Montserrat", Arial, sans-serif;
    font-weight: 800; font-size: 16px; margin-bottom: 18px;
  }
  .contact-line { font-size: 12.6px; line-height: 18px; }
  .contact-web { font-weight: 800; font-size: 17px; margin-top: 2px; }

  .brand {
    position: absolute;
    left: 832px; top: 546px;
    display: flex; align-items: center; gap: 12px;
  }
  .brand-dot {
    width: 40px; height: 40px; border-radius: 50%;
    background: var(--navy);
  }
  .brand-name {
    font-family: "Montserrat", Arial, sans-serif;
    font-weight: 800; font-size: 52px; color: var(--navy);
    letter-spacing: 1px; line-height: 1;
  }
  .brand-org {
    position: absolute; left: 832px; top: 608px; width: 330px;
    font-size: 11px; font-weight: 700; color: var(--navy);
  }
  .tagline {
    position: absolute; left: 820px; top: 650px; width: 350px;
    text-align: center;
    font-size: 28px; font-weight: 300; color: var(--cyan);
  }
  .belief {
    position: absolute; left: 820px; top: 710px; width: 350px;
    text-align: center;
    font-size: 20px; line-height: 24px; font-weight: 400; color: var(--navy);
  }
</style>
</head>
<body>
<main class="spread">
  <svg class="art" viewBox="0 0 1200 853" aria-hidden="false">
    <defs>
      <linearGradient id="teamTone" x1="0" y1="0" x2="1" y2="1">
        <stop offset="0" stop-color="#dfeef7"/>
        <stop offset="0.5" stop-color="#9fcbe4"/>
        <stop offset="1" stop-color="#4f93c4"/>
      </linearGradient>
      <linearGradient id="consultTone" x1="0" y1="0" x2="1" y2="1">
        <stop offset="0" stop-color="#f1ece4"/>
        <stop offset="0.55" stop-color="#dcc8b2"/>
        <stop offset="1" stop-color="#9ec3dc"/>
      </linearGradient>
    </defs>

    <!-- team photo area, top right -->
    <circle cx="1040" cy="200" r="300" fill="var(--navy)"/>
    <circle cx="1040" cy="200" r="284" fill="var(--paper)"/>
    <circle cx="1040" cy="200" r="276" fill="var(--cyan)"/>
    <circle cx="1040" cy="200" r="266" fill="url(#teamTone)" role="img"
            aria-label="Photo of a smiling team of doctors and nurses in white coats and scrubs"/>

    <!-- consultation photo area, bottom left -->
    <circle cx="170" cy="660" r="268" fill="var(--navy)"/>
    <circle cx="170" cy="660" r="256" fill="var(--paper)"/>
    <circle cx="170" cy="660" r="248" fill="var(--cyan)"/>
    <circle cx="170" cy="660" r="240" fill="url(#consultTone)" role="img"
            aria-label="Photo of a nurse with a clipboard speaking with an older patient"/>
  </svg>

  <section class="vision">
    <h2 class="section-title">OUR VISION IS...</h2>
    <p class="section-body"><strong>Here at the</strong> Northfield Council of Clinical Standards, we believe that the highest quality in healthcare comes from the highest quality people. We envision a care environment that is focused on quality, enabled by healthcare professionals who have been well trained to improve healthcare outcomes, and who are as passionate as we are about improving the delivery of healthcare and the performance of organizations</p>
  </section>

  <section class="mission">
    <h2 class="section-title">OUR MISSION IS...</h2>
    <p class="section-body"><strong>Our mission</strong> is to enhance quality in healthcare by transforming the professionals who work in healthcare. We aim to give you the tools and knowledge that you need to impact healthcare delivery and outcomes and to be an advocate for quality and patient safety.</p>
  </section>

  <blockquote class="quote">
    <span class="quote-mark open">“</span>
    <p class="quote-line">Don’t find fault,</p>
    <p class="quote-line strong">find a remedy.</p>
    <span class="quote-mark close">”</span>
    <p class="quote-author">HAROLD FENWICK</p>
  </blockquote>

  <address class="contact" style="font-style:normal">
    <h3 class="contact-title">CONTACT DETAILS</h3>
    <p class="contact-line">Northfield Council of Clinical Standards</p>
    <p class="contact-line">2718 West Alder Parkway</p>
    <p class="contact-line">Brookhaven, ST 40219</p>
    <p class="contact-line">Tel: 555 210 4417 &nbsp;•&nbsp; Fax: 555 210 4418</p>
    <p class="contact-web">www.brvlcouncil.org</p>
  </address>

  <div class="brand">
    <span class="brand-dot"></span>
    <span class="brand-name">BRVL</span>
  </div>
  <p class="brand-org">Northfield Council of Clinical Standards</p>
  <p class="tagline">modernize healthcare</p>
  <p class="belief">We believe that the highest quality in healthcare comes from the highest quality people.</p>
</main>
</body>
</html>
```